Design a Bold Tradeshow Backdrop for a Sustainable Cleaning Technology

We need a professional, high-impact 10' × 8' tradeshow backdrop for Vornelle®, a commercial cleaning technology company. 143.75" x 90" high and needs bleeds in the 143.75" direction for printing but the graphic area is 10' wide.

Our first event will have an audience that includes K–12 school administrators, facility managers, business officials, and custodial decision-makers. However, this backdrop will be used at multiple future trade shows across different commercial and institutional markets.

The design therefore needs to be universal rather than specifically education- or school-themed.

Our goal is to stop attendees as they walk past the booth and immediately communicate a simple message:

Safer and more sustainable cleaning can also cost substantially less than conventional cleaning chemicals.

We want the design to feel modern, innovative, clean, sustainable, credible, commercial, and premium. It should resonate with K–12 decision-makers while being equally appropriate at events serving commercial facilities, healthcare, hospitality, government, property management, transportation, and other institutional markets.

It should NOT look like a traditional janitorial supply advertisement and should not be overly busy.

The most important messages need to be understandable from approximately 10–20 feet away.

Required Messaging

The primary headline should be:

SUSTAINABLE CLEANING
DOES NOT HAVE TO BE EXPENSIVE.

Three major value propositions should be prominently displayed:

FREE
Cleaning Chemical Analysis
See how much you can save.

SAVE UP TO 60% or More
on Cleaning Chemical Costs

AS LITTLE AS $0.27/GALLON

We would also like a strong secondary message incorporated into the design:

SMARTER CLEANING.
High Performance. Low Cost. Safer.

Visual Direction — Important

Rather than showing a K–12 school hallway or other environment that limits the backdrop to the education market, we want a sophisticated, universal commercial or institutional environment.

This could be a bright, contemporary commercial facility, lobby, corridor, office environment, public building, or other premium architectural space that could reasonably represent many different types of facilities.

The environment should communicate:

Cleanliness • Safety • Sustainability • Professionalism • Efficiency • High Performance

We want someone from a school, hospital, hotel, office building, airport, government facility, or other commercial property to be able to look at the backdrop and relate the imagery to their own facility.

Please avoid imagery that makes the backdrop industry-specific.

We also want to avoid clichéd environmental imagery. The design does not need to be covered in leaves, trees, water droplets, recycling symbols, or other obvious "green" graphics to communicate sustainability. We prefer a sophisticated commercial interpretation of sustainability.

Color & Brand Direction

We want the overall color palette to stay primarily within:

Blues — consistent with our corporate identity

Greens — to reinforce sustainability, safety, efficiency, and environmental responsibility

White — strongly encouraged for clean space, contrast, and an open contemporary appearance

Black — should be limited primarily to text where necessary for readability

Please avoid making black a major background or dominant design color.

We want the finished display to have a bright, clean, sophisticated, sustainable look and feel rather than a dark or industrial appearance.

The design should use significant negative space and a strong visual hierarchy.

Less is more.

We prefer a few large, powerful messages that can be understood quickly rather than numerous small bullet points, paragraphs, or icons.

Creative Freedom

The attached concept image is provided to communicate our general direction and messaging only.

It does not need to be copied.

We are specifically running this contest because we want designers to improve upon our initial concept and show us different creative approaches to presenting the Vornelle value proposition.

We are open to creative interpretations of the commercial environment, composition, typography, use of negative space, and how the three major financial benefits are presented.

The finished design should feel like an innovative commercial technology brand, not simply another cleaning chemical company.

Corporate Logo — Very Important

We are attaching our official Vornelle® corporate logo for use in the design.

DO NOT redraw, recreate, modify, stylize, reinterpret, trace, or AI-generate the Vornelle logo.

The supplied corporate logo must be inserted directly into the artwork exactly as provided, maintaining its original proportions, colors, typography, trademark elements, and graphic design.

The logo should generally appear in the upper-left area of the backdrop but should not overwhelm the primary marketing message.

Printer Template & Graphic Sizing

We are also attaching the printer's official graphic template and instructions for the 8' × 8' tension-fabric display.

Designers should create their artwork using these supplied specifications so the winning design can be transferred directly into production.

The printer requires that the original document size not be changed, artwork be created on the designated design layer or a new layer, images be embedded, text be converted to outlines, and the finished production artwork be supplied as a PDF.

Please pay particular attention to the bleed area, finished size, and safe artwork area when positioning important text, graphics, and the corporate logo.

Physical Booth Context

The backdrop will sit behind an 8' tradeshow table.

The complete booth will also contain:

A blue stretch tablecloth with the Vornelle corporate logo
BrevoMax and Vornelle product containers and samples on the table
An HulaDrent chemical mixing/dilution station displayed on an elevated stand to the left
A television/monitor to the right demonstrating our online ROI cost-savings calculator

Because these other booth elements will explain our products and technology in greater detail, the backdrop should NOT attempt to explain everything we do.

Its primary purpose is to stop traffic, establish the Vornelle brand, and communicate our core economic and sustainability value proposition.

Final Deliverables

The winning designer must provide artwork properly sized and positioned using our supplied 8' × 8' tension-fabric display template.

Final files should include:

Print-ready, high-resolution PDF
Editable source/vector artwork
All images embedded
Fonts converted to outlines
Artwork correctly positioned within the supplied printer template
Original Vornelle corporate logo incorporated without modification
The 3–5 Second Test

This is perhaps the most important requirement.

Someone walking down a tradeshow aisle should be able to look at the backdrop for 3–5 seconds and understand:

Vornelle offers safer, sustainable, high-performance commercial cleaning — at a lower cost.

The three offers we particularly want them to remember are:

FREE CHEMICAL ANALYSIS

SAVE UP TO 60%

AS LITTLE AS $0.27/GALLON

The overall takeaway should be:

Sustainable cleaning does not have to cost more.

We want the winning design to make that message immediately understandable, credible, and memorable.

Colors
0054AA
0677BA
7BADD7
CADEEF
E8F1F8
0094D4
00A9DD
6FCCEA
C7EBF8
E9F6FB
00AB8E
00BBA5
67D7C9
C6EFE9
E9F9F6
59FF00
82FF00
B8FF75
E3FFCB
F4FFEA

```html
<!DOCTYPE html>
<html lang="en">
<head>
<meta charset="utf-8">
<title>Vornelle – Sustainable Cleaning Backdrop</title>
<link href="https://fonts.googleapis.com/css2?family=Open+Sans:wght@400;600;700;800&display=swap" rel="stylesheet">
<style>
  :root {
    --white: #ffffff;
    --navy: #252266;
    --panel-blue-start: #1b70c2;
    --panel-blue-end: #2b2c78;
    --green: #3bb54a;
    --sky: #29a7e1;
    --ink: #1a1a1a;
    --photo-light: #d3dde6;
    --photo-mid: #b9b3a8;
    --photo-warm: #a8866a;
  }
  html, body {
    margin: 0;
    padding: 0;
    width: 1200px;
    height: 1200px;
    overflow: hidden;
    background: var(--white);
  }
  .backdrop {
    position: relative;
    width: 1200px;
    height: 1200px;
    overflow: hidden;
    font-family: "Open Sans", Arial, sans-serif;
    background: var(--white);
  }
  .backdrop-shapes {
    position: absolute;
    inset: 0;
  }
  .brand-name {
    position: absolute;
    left: 56px;
    top: 176px;
    margin: 0;
    font-weight: 800;
    font-size: 64px;
    line-height: 1;
    color: var(--ink);
  }
  .secondary-message {
    position: absolute;
    right: 95px;
    top: 70px;
    margin: 0;
    text-align: right;
    color: var(--white);
    font-weight: 700;
    font-size: 41px;
    line-height: 49px;
  }
  .headline {
    position: absolute;
    left: 54px;
    top: 487px;
    margin: 0;
    color: var(--white);
    font-weight: 800;
    text-transform: uppercase;
  }
  .headline span { display: block; white-space: nowrap; }
  .headline .line-lead { font-size: 70px; line-height: 88px; }
  .headline .line-key { font-size: 90px; line-height: 86px; }
  .headline .line-tail { font-size: 58px; line-height: 69px; }

  .offer {
    position: absolute;
    color: var(--white);
    display: flex;
    gap: 20px;
  }
  .offer-icon { flex: none; }
  .offer-title {
    margin: 0;
    font-weight: 800;
    font-size: 56px;
    line-height: 56px;
  }
  .offer-copy {
    margin: 2px 0 0;
    font-weight: 400;
    font-size: 24px;
    line-height: 28px;
  }
  .offer-analysis { left: 52px; top: 980px; }
  .offer-save { left: 426px; top: 980px; }
  .offer-save .offer-copy { font-weight: 600; }
  .offer-price { left: 852px; top: 978px; align-items: center; }
  .price-symbol {
    font-weight: 800;
    font-size: 104px;
    line-height: 1;
  }
  .price-detail { display: flex; flex-direction: column; }
  .price-label { font-size: 24px; line-height: 27px; font-weight: 600; }
  .price-value { font-size: 56px; line-height: 54px; font-weight: 800; }
</style>
</head>
<body>
<main class="backdrop">
  <svg class="backdrop-shapes" width="1200" height="1200" viewBox="0 0 1200 1200">
    <defs>
      <linearGradient id="photo-tone" x1="0" y1="0" x2="0.4" y2="1">
        <stop offset="0" stop-color="var(--photo-light)"/>
        <stop offset="0.55" stop-color="var(--photo-mid)"/>
        <stop offset="1" stop-color="var(--photo-warm)"/>
      </linearGradient>
      <linearGradient id="panel-blue" x1="0" y1="0" x2="1" y2="0.3">
        <stop offset="0" stop-color="var(--panel-blue-start)"/>
        <stop offset="1" stop-color="var(--panel-blue-end)"/>
      </linearGradient>
    </defs>
    <polygon class="environment-photo" role="img"
      aria-label="Photo: a smiling businesswoman pulling a rolling suitcase through a bright, glass-walled airport concourse with travellers behind her"
      points="327,0 1200,0 1200,585 748,819 471,317" fill="url(#photo-tone)"/>
    <polygon class="headline-panel" points="0,372 471,317 748,819 0,952" fill="url(#panel-blue)"/>
    <path class="tab tab-analysis" d="M0,1200 V1008 A90,90 0 0 1 90,918 H315 A90,90 0 0 1 405,1008 V1200 Z" fill="var(--navy)"/>
    <path class="tab tab-save" d="M405,1200 V939 A90,90 0 0 1 495,849 H705 A90,90 0 0 1 795,939 V1200 Z" fill="var(--green)"/>
    <path class="tab tab-price" d="M795,1200 V862 A90,90 0 0 1 885,772 H1110 A90,90 0 0 1 1200,862 V1200 Z" fill="var(--sky)"/>
  </svg>

  <p class="brand-name">Vornelle®</p>

  <p class="secondary-message">SMARTER CLEANING.<br>High Performance.<br>Low Cost. Safer.</p>

  <h1 class="headline">
    <span class="line-lead">Sustainable</span>
    <span class="line-key">Cleaning</span>
    <span class="line-tail">Does not have</span>
    <span class="line-tail">to be expensive.</span>
  </h1>

  <section class="offer offer-analysis">
    <svg class="offer-icon" width="86" height="100" viewBox="0 0 86 100" aria-hidden="true">
      <path d="M30 6 H56 M34 6 V38 L8 88 Q5 95 13 95 H73 Q81 95 78 88 L52 38 V6" fill="none" stroke="var(--white)" stroke-width="6" stroke-linejoin="round" stroke-linecap="round"/>
      <path d="M22 64 Q43 56 64 64 L74 86 Q75 89 71 89 H15 Q11 89 12 86 Z" fill="var(--white)"/>
      <circle cx="44" cy="48" r="4" fill="var(--white)"/>
      <circle cx="38" cy="76" r="5" fill="var(--navy)"/>
      <circle cx="54" cy="80" r="3" fill="var(--navy)"/>
    </svg>
    <div>
      <p class="offer-title">FREE</p>
      <p class="offer-copy">Cleaning<br>Chemical Analysis<br>See how much<br>you can save.</p>
    </div>
  </section>

  <section class="offer offer-save">
    <svg class="offer-icon" width="110" height="96" viewBox="0 0 110 96" aria-hidden="true">
      <rect x="6" y="70" width="14" height="24" fill="var(--white)"/>
      <rect x="28" y="58" width="14" height="36" fill="var(--white)"/>
      <rect x="50" y="64" width="14" height="30" fill="var(--white)"/>
      <rect x="72" y="46" width="14" height="48" fill="var(--white)"/>
      <polyline points="4,58 34,30 56,46 94,12" fill="none" stroke="var(--white)" stroke-width="7" stroke-linejoin="round"/>
      <polygon points="80,4 106,2 102,28" fill="var(--white)"/>
    </svg>
    <div>
      <p class="offer-title">SAVE</p>
      <p class="offer-copy">UP TO 60% or<br>More on Cleaning<br>Chemical Costs</p>
    </div>
  </section>

  <section class="offer offer-price">
    <span class="price-symbol" aria-hidden="true">$</span>
    <div class="price-detail">
      <span class="price-label">AS LITTLE AS</span>
      <span class="price-value">$0.27</span>
      <span class="price-label">/GALLON</span>
    </div>
  </section>
</main>
</body>
</html>
```